Business Card Design Project

HI! Can you design a business card with the logo you designed for me? I don't know what the typical order is so can you place it in the order most people do? White background and also play with a couple of colored backgrounds. Thank you!

Darnel Quesvo-Tranetti
darnel@tovenashcoaching.example
tovenashcoaching.example
555-317-4809

Target Market(s)

Women

Industry/Entity Type

Business

```html
<!DOCTYPE html>
<html lang="en">
<head>
<meta charset="utf-8">
<title>Tovenash Coaching – Business Cards</title>
<link rel="stylesheet" href="https://fonts.googleapis.com/css2?family=Open+Sans:wght@400;600&display=swap">
<style>
  :root {
    --page: #ece8e2;
    --card-white: #ffffff;
    --card-black: #0c0a0b;
    --brand-orange: #f39321;
    --brand-red: #b8202f;
    --text-light: #f4f4f4;
    --shadow: rgba(0, 0, 0, 0.22);
  }
  html, body {
    margin: 0;
    padding: 0;
    width: 1200px;
    height: 1024px;
    overflow: hidden;
    background: var(--page);
    font-family: "Open Sans", Arial, sans-serif;
  }
  .canvas {
    position: relative;
    width: 1200px;
    height: 1024px;
  }
  .card {
    position: absolute;
    left: 250px;
    width: 700px;
    height: 400px;
    border-radius: 26px;
    overflow: hidden;
    box-shadow: 0 8px 24px var(--shadow);
  }
  .card--front { top: 60px; background: var(--card-white); }
  .card--back { top: 564px; background: var(--card-black); }
  .card__art {
    position: absolute;
    inset: 0;
    width: 100%;
    height: 100%;
  }

  /* Front: brand block on white */
  .brand {
    position: absolute;
    left: 60px;
    top: 160px;
    width: 250px;
    display: flex;
    flex-direction: column;
    align-items: center;
    gap: 10px;
  }
  .brand__dot {
    width: 52px;
    height: 52px;
    border-radius: 50%;
    background: var(--brand-orange);
  }
  .brand__name {
    font-size: 24px;
    font-weight: 600;
    color: var(--brand-red);
    letter-spacing: 0.3px;
    white-space: nowrap;
  }

  /* Front: contact block on black */
  .contact {
    position: absolute;
    right: 34px;
    top: 110px;
    width: 280px;
    text-align: right;
    color: var(--text-light);
  }
  .contact__name {
    margin: 0 0 16px;
    font-size: 21px;
    font-weight: 400;
    color: var(--brand-orange);
    white-space: nowrap;
  }
  .contact__line {
    display: flex;
    justify-content: flex-end;
    align-items: center;
    gap: 8px;
    margin: 0 0 9px;
    font-size: 14px;
    white-space: nowrap;
  }
  .contact__icon {
    width: 14px;
    height: 14px;
    flex: none;
    fill: var(--brand-orange);
  }

  /* Back */
  .emblem {
    position: absolute;
    left: 50%;
    top: 38px;
    transform: translateX(-50%);
    width: 230px;
    height: 230px;
    border-radius: 50%;
    background: var(--brand-orange);
    display: flex;
    align-items: center;
    justify-content: center;
  }
  .emblem__name {
    font-size: 34px;
    font-weight: 600;
    color: var(--card-white);
  }
  .web {
    position: absolute;
    left: 0;
    right: 0;
    bottom: 58px;
    margin: 0;
    text-align: center;
    font-size: 20px;
    color: var(--text-light);
  }
  .web__domain { color: var(--brand-orange); }
</style>
</head>
<body>
<main class="canvas">

  <section class="card card--front" aria-label="Business card front">
    <svg class="card__art" viewBox="0 0 700 400" aria-hidden="true">
      <path d="M150 400 C260 382 330 330 352 248 C346 338 286 392 232 400 Z" fill="var(--brand-orange)"/>
      <path d="M436 0 C398 40 378 110 360 190 C344 262 318 334 236 392" fill="none" stroke="var(--brand-red)" stroke-width="9"/>
      <path d="M462 0 H700 V400 H232 C330 360 362 262 382 182 C402 100 422 32 462 0 Z" fill="var(--card-black)"/>
    </svg>

    <div class="brand">
      <span class="brand__dot"></span>
      <span class="brand__name">Tovenash Coaching</span>
    </div>

    <div class="contact">
      <h1 class="contact__name">Darnel Quesvo-Tranetti</h1>
      <p class="contact__line">
        555-317-4809
        <svg class="contact__icon" viewBox="0 0 24 24"><path d="M6.6 10.8a15.1 15.1 0 0 0 6.6 6.6l2.2-2.2a1 1 0 0 1 1-.25 11.4 11.4 0 0 0 3.6.57 1 1 0 0 1 1 1V20a1 1 0 0 1-1 1A17 17 0 0 1 3 4a1 1 0 0 1 1-1h3.5a1 1 0 0 1 1 1c0 1.25.2 2.45.57 3.57a1 1 0 0 1-.25 1z"/></svg>
      </p>
      <p class="contact__line">
        darnel@tovenashcoaching.example
        <svg class="contact__icon" viewBox="0 0 24 24"><path d="M2 5h20v14H2z M4 7v.4l8 5 8-5V7z" fill-rule="evenodd"/></svg>
      </p>
      <p class="contact__line">
        tovenashcoaching.example
        <svg class="contact__icon" viewBox="0 0 24 24"><path d="M12 2a10 10 0 1 0 0 20 10 10 0 0 0 0-20zm0 2c.9 0 2.2 1.9 2.7 5H9.3C9.8 5.9 11.1 4 12 4zM9.1 11h5.8a18 18 0 0 1 0 2H9.1a18 18 0 0 1 0-2zM4.1 11h3a20 20 0 0 0 0 2h-3a8 8 0 0 1 0-2zm12.8 0h3a8 8 0 0 1 0 2h-3a20 20 0 0 0 0-2zM12 20c-.9 0-2.2-1.9-2.7-5h5.4c-.5 3.1-1.8 5-2.7 5z"/></svg>
      </p>
    </div>
  </section>

  <section class="card card--back" aria-label="Business card back">
    <div class="emblem">
      <span class="emblem__name">Tovenash</span>
    </div>
    <p class="web">www.<span class="web__domain">tovenashcoaching</span>.example</p>
  </section>

</main>
</body>
</html>
```